Internet Of Things brochure

Need to create a brochure with a common theme to our website and the last 2 pages of the attached file. All the contect is in the file that I have attached.
website www.norvalegroup.com.au

Industry/Entity Type

Internet

```html
<!DOCTYPE html>
<html lang="en">
<head>
<meta charset="utf-8">
<title>Norvale Group – Internet of Things Brochure</title>
<link rel="stylesheet" href="https://fonts.googleapis.com/css2?family=Exo+2:wght@400;500;600&display=swap">
<style>
  :root{
    --bg:#ebebeb;
    --ink:#0b0b0d;
    --navy:#2f3a72;
    --purple:#3d2a5e;
    --violet:#514079;
    --paper:#f6f6f8;
    --text-dark:#1c1c24;
    --white:#ffffff;
  }
  *{box-sizing:border-box;margin:0;padding:0}
  html,body{width:1200px;height:1000px;overflow:hidden;background:var(--bg)}
  body{font-family:"Exo 2",sans-serif;position:relative}
  .spread{position:absolute;left:60px;top:118px;width:1080px;height:764px;display:flex;box-shadow:0 18px 40px rgba(0,0,0,.18)}
  .page{position:relative;width:540px;height:764px;background:var(--paper);overflow:hidden}
  .page + .page{border-left:1px solid #cfcfd4}
  .header{position:absolute;left:0;top:0;width:100%;background:var(--ink);display:flex;align-items:center;gap:22px;padding:0 22px;color:var(--white)}
  .brand{display:flex;align-items:center;gap:6px;font-weight:600;font-size:13px;letter-spacing:.5px}
  .brand-mark{width:12px;height:12px;background:var(--white)}
  .partner-badge{width:22px;height:22px;border-radius:50%;background:#d9d9de}
  .cloud-name{font-weight:400;font-size:15px}
  .contact{position:absolute;right:22px;text-align:right;font-size:10px;line-height:1.35;font-weight:500;color:var(--white)}
  .block{position:absolute;padding:22px 24px;font-size:11.5px;line-height:1.42;font-weight:500}
  .block.light{background:var(--paper);color:var(--text-dark)}
  .block.navy{background:var(--navy);color:var(--white)}
  .block.purple{background:var(--purple);color:var(--white)}
  .block.violet{background:var(--violet);color:var(--white)}
  .photo{position:absolute}
  .photo-engineer-field{background:linear-gradient(160deg,#5f7fa8,#2a3c57 60%,#c9a23a)}
  .photo-fleet{background:linear-gradient(150deg,#d9dadd,#8f949b 55%,#3f4a52)}
  .photo-traffic{background:linear-gradient(100deg,#0c1424,#27456b 50%,#0d1a2d)}
  .photo-tablet{background:linear-gradient(160deg,#6e6e74,#3b3d44 60%,#9aa0a8)}
  .photo-factory{background:linear-gradient(130deg,#c9a82a,#6b6d73 45%,#2c3d5e)}
  .photo-towers{background:linear-gradient(170deg,#050507,#1a1b22 55%,#4a4c55)}
</style>
</head>
<body>
<main class="spread">
  <section class="page page-left">
    <header class="header" style="height:70px">
      <div class="brand"><span class="brand-mark"></span>NORVALE GROUP</div>
      <span class="partner-badge"></span>
      <span class="cloud-name">Nimbus Cloud</span>
      <div class="contact">P: 1300 555 019<br>A: 48 - 52 Harbour Road<br>Westmead, NSW, 2145<br>W: www.norvalegroup.com.au</div>
    </header>
    <div class="photo photo-engineer-field" role="img" aria-label="Engineer in hard hat and safety vest using a tablet beside wind turbines" style="left:0;top:70px;width:300px;height:230px"></div>
    <div class="block navy" style="left:300px;top:70px;width:240px;height:230px;padding-top:50px">
      Innovate and transform your business with IoT solutions Put the Internet of Things (IoT) to work for you. Drive digital transformation across your business with end-to-end IoT solutions that can be tailored for any need, helping make informed decisions, optimise operations, reduce costs, and create new revenue streams.
    </div>
    <div class="block light" style="left:0;top:300px;width:270px;height:200px">
      Remote monitoring Reduce manual, time-intensive processes when you connect and monitor your business devices and assets. Access, analyse, and use previously untapped data to automate business processes and trigger automatic alerts and actions, such as remote diagnostics, to help increase efficiencies and decrease costs.
    </div>
    <div class="photo photo-fleet" role="img" aria-label="Tablet showing a fleet management dashboard with a map and KPI tiles" style="left:270px;top:300px;width:270px;height:290px"></div>
    <div class="photo photo-traffic" role="img" aria-label="Night traffic with blurred car light trails" style="left:0;top:500px;width:270px;height:90px"></div>
    <div class="block purple" style="left:0;top:590px;width:540px;height:174px;padding-top:28px">
      Connected vehicle Transform the driving experience while innovating automotive manufacturing with the Nimbus Connected Vehicle Platform. From Vela and predictive services to cloud-enhanced advanced driver assistance systems, use industry-leading technology to create connected and differentiated driving experiences that increase customer loyalty and reveal new revenue opportunities.
    </div>
  </section>

  <section class="page page-right">
    <header class="header" style="height:90px">
      <div class="brand"><span class="brand-mark"></span>NORVALE GROUP</div>
      <span class="partner-badge"></span>
      <span class="cloud-name">Nimbus Cloud</span>
      <div class="contact">P: 1300 555 019<br>A: 48 - 52 Harbour Road<br>Westmead, NSW, 2145<br>W: www.norvalegroup.com.au</div>
    </header>
    <div class="block light" style="left:0;top:90px;width:290px;height:240px;padding-top:34px">
      Connected field service Detect, troubleshoot, and resolve issues remotely before your customers know there's a problem. When an issue escalates, automatically dispatch the best technician and tools to deliver a first-time fix.
    </div>
    <div class="photo photo-tablet" role="img" aria-label="Hands holding a rugged tablet showing an asset map dashboard" style="left:290px;top:90px;width:250px;height:240px"></div>
    <div class="photo photo-factory" role="img" aria-label="Technician with ear protection using a tablet next to a yellow robotic arm" style="left:0;top:330px;width:270px;height:230px"></div>
    <div class="block violet" style="left:270px;top:330px;width:270px;height:230px;padding-top:40px">
      Predictive maintenance Anticipate your maintenance needs to prevent equipment failures and avoid unscheduled downtime. Analyse streaming data to quickly assess conditions, recognize warning signs, and preemptively service equipment before costly repairs are needed.
    </div>
    <div class="block light" style="left:0;top:560px;width:270px;height:204px">
      Smart buildings Reduce costs, improve efficiencies, and increase occupant satisfaction and productivity using IoT. Gain actionable insights and control by connecting building devices and systems, collecting data, and running powerful analytics.
    </div>
    <div class="photo photo-towers" role="img" aria-label="Two glass skyscrapers lit at night against a dark sky" style="left:270px;top:560px;width:270px;height:204px"></div>
  </section>
</main>
</body>
</html>
```